Carpet cleaning company wants business card

Need an exciting new fresh design for business cards for my carpet cleaning /pest control business
www.tidewellhomecare.com.au
Can design include a lined section for quoting or information? Thanks !

```html
<!DOCTYPE html>
<html lang="en">
<head>
<meta charset="utf-8">
<title>Tidewell Home Care – Business Card</title>
<link rel="stylesheet" href="https://fonts.googleapis.com/css2?family=Montserrat:wght@400;600;700;800&display=swap">
<style>
  :root {
    --brand-blue: #0f4fa0;
    --brand-red: #e8362d;
    --ink: #1c1c1c;
    --card: #ffffff;
    --backdrop: #2a3440;
  }
  * { box-sizing: border-box; margin: 0; padding: 0; }
  html, body {
    width: 1200px; height: 900px; overflow: hidden;
    background: var(--backdrop);
    font-family: "Montserrat", sans-serif;
    color: var(--ink);
  }
  .card {
    position: absolute;
    background: var(--card);
    border-radius: 16px;
    overflow: hidden;
    box-shadow: 0 6px 18px rgba(0,0,0,0.35);
  }
  .card--front { left: 286px; top: 57px; width: 600px; height: 361px; }
  .card--back  { left: 283px; top: 470px; width: 607px; height: 366px; }

  .wordmark {
    font-family: "Montserrat", sans-serif;
    font-weight: 800;
    color: var(--brand-blue);
    letter-spacing: -0.5px;
    white-space: nowrap;
  }
  .card--front .wordmark { position: absolute; left: 25px; top: 38px; font-size: 34px; }
  .card--back .wordmark {
    position: absolute; left: 0; right: 0; top: 150px;
    text-align: center; font-size: 48px;
  }

  .name-marker {
    position: absolute; left: 0; top: 180px; width: 12px; height: 35px;
    background: var(--brand-red);
  }
  .holder { position: absolute; left: 25px; top: 176px; }
  .holder__name { font-size: 25px; font-weight: 700; line-height: 1.1; }
  .holder__first { color: var(--brand-red); }
  .holder__last { color: var(--brand-blue); }
  .holder__role { font-size: 14px; margin-left: 2px; line-height: 1.2; }

  .address { position: absolute; left: 25px; top: 232px; font-size: 14px; line-height: 17px; }

  .contacts { position: absolute; left: 25px; top: 283px; list-style: none; font-size: 14.5px; }
  .contacts li { display: flex; align-items: center; height: 18.5px; }
  .contacts svg { width: 12px; height: 12px; margin-right: 8px; fill: var(--brand-blue); }

  .services { position: absolute; right: 29px; top: 150px; text-align: right; }
  .services__title { color: var(--brand-red); font-weight: 700; font-size: 17px; margin-bottom: 2px; }
  .services__list { list-style: none; font-size: 14px; }
  .services__list li { height: 20.4px; line-height: 20.4px; padding-right: 12px; position: relative; }
  .services__list li::after {
    content: ""; position: absolute; right: -1px; top: 9px;
    width: 4px; height: 4px; border-radius: 50%; background: var(--brand-red);
  }

  .edge-stripe { position: absolute; left: 0; bottom: 0; width: 600px; height: 11px; }
</style>
</head>
<body>

<section class="card card--front" aria-label="Business card front">
  <div class="wordmark">Tidewell Home Care</div>

  <div class="name-marker"></div>
  <div class="holder">
    <p class="holder__name"><span class="holder__first">Marlo</span> <span class="holder__last">Quenby</span></p>
    <p class="holder__role">Owner</p>
  </div>

  <p class="address">48 Harbourview Road, Suite 6<br>Norwood, SA 5067</p>

  <ul class="contacts">
    <li><svg viewBox="0 0 12 12"><path d="M1 4 Q6 0 11 4 L10 5.5 L8 5 L8 4 Q6 3.2 4 4 L4 5 L2 5.5 Z M3 6 L9 6 L10.5 11 L1.5 11 Z"/></svg>07 5550 2184</li>
    <li><svg viewBox="0 0 12 12"><path d="M0.5 2.5 H11.5 V10 H0.5 Z M1.2 3 L6 7 L10.8 3" stroke="#fff" stroke-width="0.9"/></svg>info@tidewellhomecare.com.au</li>
    <li><svg viewBox="0 0 12 12"><circle cx="6" cy="6" r="5.5"/><path d="M3 4 Q5 3 5 5 Q4 7 6 8 L5 10.5 M8 2 Q7 4 9 5 L10.5 6" stroke="#fff" stroke-width="0.9" fill="none"/></svg>www.tidewellhomecare.com.au</li>
  </ul>

  <div class="services">
    <p class="services__title">Our Services</p>
    <ul class="services__list">
      <li>Residential Carpet Cleaning</li>
      <li>Commercial Carpet Cleaning</li>
      <li>Vacate Carpet Cleaning &amp; Pest Control</li>
      <li>Pest Control</li>
      <li>Furniture and Upholstery Cleaning</li>
      <li>Tile and Grout Cleaning</li>
      <li>Water Extraction Service</li>
      <li>Mats and Rug Cleaning</li>
    </ul>
  </div>

  <svg class="edge-stripe" viewBox="0 0 600 11" preserveAspectRatio="none" aria-hidden="true">
    <polygon points="0,0 396,0 385,11 0,11" fill="var(--brand-blue)"/>
    <polygon points="402,0 600,0 600,11 391,11" fill="var(--brand-red)"/>
  </svg>
</section>

<section class="card card--back" aria-label="Business card back">
  <div class="wordmark">Tidewell Home Care</div>
</section>

</body>
</html>
```